PACKAGING WRAPPER DESIGN For toilet rolls

We are a toilet paper supplier and require a modern looking packaging wrapper for toilet rolls. These are paper wrappers that individually wrap around a toilet roll. Additional need a matching carton as well. Require a modern looking wrapper and carton. This is for a new product line, however if all good would consider a longer term to overhaul existing product line as well.

Colors
0255a3
3276b5
959595
dcdcdc

Requirements
Must have
• Brand Name is Corvin (refer to file attached) must have that brand name.
• This wrapper will be part of our PREMIUM range. So must have
• Corvin Premium Toilet Rolls as the wording. I have attached samples of a toilet wrapper for another line as well as a carton to give you an idea of what I am looking at and the layout etc..

```html
<!DOCTYPE html>
<html lang="en">
<head>
<meta charset="utf-8">
<title>Corvin Premium Toilet Rolls – Wrapper and Carton</title>
<link rel="stylesheet" href="https://fonts.googleapis.com/css2?family=Libre+Baskerville:wght@400&display=swap">
<style>
  :root{
    --stage:#eeeeee;
    --paper:#ffffff;
    --brand-blue:#0255a3;
    --brand-blue-light:#3276b5;
    --brand-grey:#959595;
    --brand-grey-light:#dcdcdc;
    --text-light:#ffffff;
  }
  *{margin:0;padding:0;box-sizing:border-box}
  html,body{width:1200px;height:1200px;overflow:hidden;background:var(--stage)}
  body{position:relative;font-family:"Libre Baskerville",Georgia,serif;color:var(--text-light)}

  .panel{position:absolute;overflow:hidden;background:var(--brand-blue);box-shadow:0 6px 18px rgba(0,0,0,.12)}
  .top-band{position:absolute;left:0;top:0;width:100%;height:70px;background:var(--paper);border-bottom:8px solid var(--brand-grey-light)}
  .meadow{position:absolute;left:0;bottom:0;width:100%}

  /* carton */
  .carton-front{left:90px;top:70px;width:580px;height:540px}
  .carton-side{left:670px;top:70px;width:440px;height:540px;background:var(--brand-blue-light)}
  .carton-front .meadow,.carton-side .meadow{height:80px;background:linear-gradient(to top,rgba(149,149,149,.75),rgba(149,149,149,0))}

  .title-block{position:absolute;right:46px;text-align:right;line-height:1.15}
  .carton-front .title-block{top:120px}
  .tagline{font-size:34px}
  .brand-name{font-size:112px;line-height:1;margin-top:6px;letter-spacing:1px}
  .spec{font-size:15px;line-height:1.7;margin-top:18px}
  .recycled{display:inline-flex;align-items:center;gap:8px}
  .recycled-dot{width:14px;height:14px;border-radius:50%;border:2px solid var(--text-light)}
  .web{position:absolute;left:40px;bottom:24px;font-size:19px;letter-spacing:.5px}

  .carton-fields{position:absolute;left:30px;top:160px;width:380px}
  .field{display:flex;align-items:center;justify-content:flex-end;gap:14px;margin-bottom:14px;font-size:14px}
  .field-box{width:200px;height:34px;border-radius:8px;background:var(--brand-grey-light)}
  .handling-icons{position:absolute;right:40px;top:330px;display:flex;gap:34px}
  .handling-icon{width:62px;height:78px;border:2px solid var(--text-light);border-radius:6px;display:flex;flex-direction:column;align-items:center;justify-content:center;gap:6px;font-size:7px;text-align:center}

  /* wrapper */
  .wrapper{left:90px;top:670px;width:1020px;height:470px}
  .wrapper .top-band{border-bottom-color:var(--brand-grey)}
  .wrapper .meadow{height:70px;background:linear-gradient(to top,rgba(149,149,149,.8),rgba(149,149,149,0))}
  .wrapper .title-block{right:250px;top:110px}
  .wrapper .tagline{font-size:36px}
  .wrapper .brand-name{font-size:112px}
</style>
</head>
<body>

<section class="panel carton-front" aria-label="Carton front">
  <div class="top-band"></div>
  <div class="title-block">
    <p class="tagline">Premium<br>Toilet Rolls</p>
    <p class="brand-name">Corvin</p>
    <p class="spec">400 x 2 Ply Sheets (11cm x 10cm)<br>Re-order Code 00XXX00<br><span class="recycled"><span class="recycled-dot"></span>100% Recycled</span></p>
  </div>
  <div class="meadow" role="img" aria-label="Meadow of flower and grass silhouettes"></div>
  <p class="web">www.corvin.com.au</p>
</section>

<section class="panel carton-side" aria-label="Carton side">
  <div class="top-band"></div>
  <div class="carton-fields">
    <div class="field"><span>Carton Dimension:</span><span class="field-box"></span></div>
    <div class="field"><span>Net Weight:</span><span class="field-box"></span></div>
    <div class="field"><span>Gross Weight:</span><span class="field-box"></span></div>
  </div>
  <div class="handling-icons">
    <div class="handling-icon">
      <svg width="30" height="30" viewBox="0 0 30 30" aria-hidden="true"><rect x="9" y="6" width="12" height="10" fill="#fff"/><path d="M3 16 Q8 26 15 26 Q22 26 27 16" fill="none" stroke="#fff" stroke-width="3"/></svg>
      <span>Handle With Care</span>
    </div>
    <div class="handling-icon">
      <svg width="30" height="30" viewBox="0 0 30 30" aria-hidden="true"><path d="M3 14 Q15 0 27 14Z" fill="#fff"/><path d="M15 14V24 Q15 27 12 26" fill="none" stroke="#fff" stroke-width="2"/></svg>
      <span>Keep Dry</span>
    </div>
    <div class="handling-icon">
      <svg width="30" height="30" viewBox="0 0 30 30" aria-hidden="true"><path d="M15 3 L25 14 H19 V27 H11 V14 H5Z" fill="#fff"/></svg>
      <span>Upward</span>
    </div>
  </div>
  <div class="meadow" role="img" aria-label="Meadow of flower and grass silhouettes with butterflies"></div>
</section>

<section class="panel wrapper" aria-label="Toilet roll wrapper">
  <div class="top-band"></div>
  <div class="title-block">
    <p class="tagline">Premium<br>Toilet Rolls</p>
    <p class="brand-name">Corvin</p>
    <p class="spec">400 x 2 Ply Sheets (11cm x 10cm)<br>Re-order Code 00XXX00</p>
  </div>
  <div class="meadow" role="img" aria-label="Meadow of flower and grass silhouettes with butterflies"></div>
</section>

</body>
</html>
```